Placing my newer logo on my existing business card

I have a business card that I had you guys do years ago, then I changed my logo, I love both my business card and my logo. The challenge is both my logo and my business card are very similar in color. So I'm not sure how to make my logo stand out.

Sick

```html
<!DOCTYPE html>
<html lang="en">
<head>
<meta charset="utf-8">
<title>Harbor Wellness &amp; Hormone Clinic – Business Cards</title>
<link href="https://fonts.googleapis.com/css2?family=Cinzel:wght@600&family=EB+Garamond:wght@400;500&family=Great+Vibes&display=swap" rel="stylesheet">
<style>
  :root {
    --bg: #e9e6e3;
    --copper: #b0643c;
    --copper-light: #d39a80;
    --maroon: #5b2a2f;
    --sky-top: #ffffff;
    --sky-bottom: #8fcde8;
    --brand: #b8502f;
    --ink: #1d1d1f;
    --rule: #4a4a4a;
  }
  * { box-sizing: border-box; margin: 0; padding: 0; }
  html, body { width: 1200px; height: 900px; overflow: hidden; }
  body {
    background: var(--bg);
    position: relative;
    font-family: "EB Garamond", Georgia, serif;
    color: var(--ink);
  }
  .card {
    position: absolute;
    width: 640px;
    height: 366px;
    box-shadow: 0 10px 24px rgba(0,0,0,.25);
    overflow: hidden;
  }
  /* Appointment card */
  .card--appointment {
    left: 50px; top: 60px;
    background: linear-gradient(160deg, var(--copper) 0%, var(--copper) 45%, var(--copper-light) 62%, var(--maroon) 85%);
    padding: 30px;
  }
  .appointment__panel {
    width: 100%; height: 100%;
    background: linear-gradient(180deg, var(--sky-top) 0%, var(--sky-bottom) 100%);
    display: flex; flex-direction: column; align-items: center;
    padding-top: 26px;
  }
  .brand {
    display: flex; align-items: center; gap: 12px;
    font-family: "Cinzel", "Times New Roman", serif;
    font-weight: 600;
    color: var(--brand);
    text-transform: uppercase;
    line-height: 1.05;
    letter-spacing: .06em;
  }
  .brand__dot {
    flex: none;
    border-radius: 50%;
    background: var(--brand);
  }
  .card--appointment .brand { font-size: 19px; }
  .card--appointment .brand__dot { width: 30px; height: 30px; }
  .appointment__title {
    margin-top: 20px;
    font-family: "Cinzel", "Times New Roman", serif;
    font-weight: 600;
    font-size: 25px;
    letter-spacing: .05em;
  }
  .appointment__fields {
    margin-top: 22px;
    width: 500px;
    display: flex; align-items: flex-end; gap: 10px;
    font-size: 24px;
  }
  .field__line {
    flex: 1;
    border-bottom: 1.5px solid var(--ink);
    height: 20px;
  }
  .appointment__tagline {
    margin-top: 14px;
    font-family: "Great Vibes", cursive;
    font-size: 44px;
    line-height: 1;
  }
  /* Contact card */
  .card--contact {
    left: 510px; top: 474px;
    background: linear-gradient(180deg, var(--sky-top) 0%, var(--sky-bottom) 100%);
  }
  .contact__ribbon {
    position: absolute; right: 0; top: 0;
    width: 260px; height: 366px;
  }
  .contact__body {
    position: absolute; left: 40px; top: 70px;
    width: 400px;
    display: flex; flex-direction: column; align-items: center;
    text-align: center;
  }
  .card--contact .brand { font-size: 26px; }
  .card--contact .brand__dot { width: 40px; height: 40px; }
  .contact__lines { margin-top: 20px; font-size: 19px; line-height: 1.3; }
  .contact__label { color: var(--brand); }
  .contact__divider {
    margin: 12px 0;
    width: 380px;
    display: flex; align-items: center; gap: 10px;
  }
  .contact__divider span { flex: 1; height: 1px; background: var(--rule); }
  .contact__divider i { width: 7px; height: 7px; border-radius: 50%; background: var(--ink); }
  .contact__address { font-size: 19px; line-height: 1.3; }
</style>
</head>
<body>

<section class="card card--appointment" aria-label="Appointment card">
  <div class="appointment__panel">
    <div class="brand">
      <span class="brand__dot"></span>
      <span>Harbor Wellness<br>&amp; Hormone Clinic</span>
    </div>
    <p class="appointment__title">APPOINTMENT ON...</p>
    <div class="appointment__fields">
      <span>Time</span><span class="field__line"></span>
      <span>Date</span><span class="field__line"></span>
    </div>
    <p class="appointment__tagline">Let’s Make it Happen</p>
  </div>
</section>

<section class="card card--contact" aria-label="Contact card">
  <svg class="contact__ribbon" viewBox="0 0 260 366" role="img" aria-label="Flowing copper ribbon swirls over a copper-to-maroon curved band">
    <defs>
      <linearGradient id="bandFill" x1="0" y1="0" x2="1" y2="1">
        <stop offset="0" stop-color="#b0643c"/>
        <stop offset=".45" stop-color="#d39a80"/>
        <stop offset=".8" stop-color="#5b2a2f"/>
      </linearGradient>
    </defs>
    <path d="M40 0 C130 10 60 150 120 250 C150 300 200 320 260 336 L260 0 Z" fill="url(#bandFill)"/>
  </svg>

  <div class="contact__body">
    <div class="brand">
      <span class="brand__dot"></span>
      <span>Harbor Wellness<br>&amp; Hormone Clinic</span>
    </div>
    <p class="contact__lines">
      <span class="contact__label">PH:</span> (555) 014-2286 | <span class="contact__label">FX:</span> (555) 014-2287<br>
      harborwellnessclinic.example
    </p>
    <div class="contact__divider"><span></span><i></i><span></span></div>
    <p class="contact__address">1200 maple ave ste#5<br>riverton co 80000</p>
  </div>
</section>

</body>
</html>
```